Criação de Folder para Planejamento de Eventos
" Nós trabalhamos com eventos de adultos, eventos infantis e também nos flexibilizamos para locação de nosso espaço, sem nosso buffet. "

```html
<!DOCTYPE html>
<html lang="pt-BR">
<head>
<meta charset="utf-8">
<title>Espaço Aurora — Folder de Eventos</title>
<link rel="stylesheet" href="https://fonts.googleapis.com/css2?family=Montserrat:wght@400;600;700&display=swap">
<style>
  :root {
    --page: #cfcfd1;
    --ink: #141416;
    --panel: #1c1c1f;
    --panel-soft: #26262a;
    --red: #b3121b;
    --red-deep: #6e0c12;
    --white: #f4f4f4;
    --muted: #b9b9bd;
  }
  * { box-sizing: border-box; margin: 0; padding: 0; }
  html, body { width: 1200px; height: 1200px; overflow: hidden; }
  body {
    background: var(--page);
    font-family: "Montserrat", sans-serif;
    color: var(--white);
    position: relative;
  }
  .brochure {
    position: absolute;
    left: 30px; top: 400px;
    width: 1140px; height: 400px;
    background: var(--panel);
    overflow: hidden;
  }
  .brochure__art { position: absolute; inset: 0; }
  .fold { position: absolute; top: 0; bottom: 0; width: 1px; background: rgba(255,255,255,.06); }
  .fold--one { left: 380px; }
  .fold--two { left: 760px; }

  .services { position: absolute; left: 26px; top: 118px; width: 320px; }
  .services__title {
    font-weight: 700; font-size: 12px; line-height: 1.25;
    letter-spacing: .5px; text-transform: uppercase;
  }
  .services__list { list-style: none; margin-top: 8px; }
  .services__list li { font-size: 8.5px; line-height: 1.5; color: var(--muted); }

  .food-grid {
    position: absolute; left: 26px; top: 232px;
    display: grid; grid-template-columns: repeat(4, 72px); grid-auto-rows: 40px; gap: 6px;
  }
  .food-grid__item {
    border: 2px solid var(--white);
    background: linear-gradient(135deg, #e7a43a, #b5621c);
  }
  .food-grid__item--brown { background: linear-gradient(135deg, #7a4524, #3f2212); }
  .food-grid__item--red { background: linear-gradient(135deg, #d98a3a, #a8321e); }

  .contact { position: absolute; left: 420px; top: 232px; width: 300px; }
  .contact__title { font-weight: 700; font-size: 12px; letter-spacing: .5px; text-transform: uppercase; }
  .contact__row { display: flex; align-items: center; gap: 7px; margin-top: 9px; }
  .contact__icon { width: 12px; height: 12px; flex: none; }
  .contact__phone { font-weight: 700; font-size: 14px; color: var(--red); }
  .contact__line { font-size: 8.5px; color: var(--muted); }
  .contact__address { margin-top: 12px; font-size: 8.5px; line-height: 1.5; color: var(--muted); }

  .brand-name {
    position: absolute; font-weight: 600; color: var(--white);
    font-size: 15px; letter-spacing: 1px; text-transform: uppercase;
  }
  .brand-name--inside { left: 560px; top: 60px; }
  .brand-name--cover { right: 26px; bottom: 40px; color: var(--red); font-size: 14px; }

  .cover-tagline {
    position: absolute; left: 790px; top: 22px; width: 230px;
    font-weight: 700; font-size: 11px; line-height: 1.35; text-transform: uppercase; letter-spacing: .4px;
  }
</style>
</head>
<body>
  <main class="brochure">
    <svg class="brochure__art" viewBox="0 0 1140 400" width="1140" height="400" aria-hidden="false">
      <defs>
        <linearGradient id="hallTone" x1="0" y1="0" x2="1" y2="1">
          <stop offset="0" stop-color="#4a4660"/>
          <stop offset=".45" stop-color="#d9d4dc"/>
          <stop offset="1" stop-color="#8a7f78"/>
        </linearGradient>
        <linearGradient id="venueTone" x1="0" y1="0" x2="1" y2="0">
          <stop offset="0" stop-color="#2d1e4f"/>
          <stop offset=".5" stop-color="#7b4fc4"/>
          <stop offset="1" stop-color="#3a2a5c"/>
        </linearGradient>
      </defs>

      <!-- inside spread: decorated reception hall -->
      <polygon role="img" aria-label="Foto do salão decorado com arranjo de flores e mesa de doces"
               points="150,0 760,0 760,212 318,212" fill="url(#hallTone)"/>
      <polygon points="90,0 150,0 318,212 250,212" fill="var(--panel-soft)"/>
      <polygon points="118,0 126,0 296,212 286,212" fill="var(--red)"/>
      <polygon points="318,212 760,212 760,224 330,224" fill="var(--red-deep)"/>

      <!-- left panel bottom accents -->
      <polygon points="0,360 120,320 140,326 0,374" fill="var(--red)"/>
      <polygon points="0,380 180,330 190,336 0,400" fill="var(--panel-soft)"/>

      <!-- middle panel bottom accent -->
      <polygon points="560,400 760,310 760,330 600,400" fill="var(--panel-soft)"/>

      <!-- cover -->
      <polygon points="1060,0 1140,0 1140,44" fill="var(--red)"/>
      <polygon role="img" aria-label="Foto da fachada do espaço iluminada em tons de roxo à noite"
               points="760,112 1140,82 1140,268 930,300 760,256" fill="url(#venueTone)"/>
      <polygon points="760,256 930,300 1140,268 1140,290 930,324 760,280" fill="var(--red)"/>
      <polygon points="760,280 930,324 1140,290 1140,320 920,352 760,300" fill="var(--red-deep)"/>
    </svg>

    <div class="fold fold--one"></div>
    <div class="fold fold--two"></div>

    <span class="brand-name brand-name--inside">Espaço Aurora</span>

    <section class="services">
      <h2 class="services__title">Serviços próprios<br>e parcerias</h2>
      <ul class="services__list">
        <li>Buffet completo adulto</li>
        <li>Festas infantis temáticas</li>
        <li>Decoração e iluminação</li>
        <li>Bolos e doces finos</li>
        <li>Locação do espaço</li>
      </ul>
    </section>

    <div class="food-grid">
      <div class="food-grid__item" role="img" aria-label="Foto de salgados dourados"></div>
      <div class="food-grid__item food-grid__item--brown" role="img" aria-label="Foto de doces de chocolate"></div>
      <div class="food-grid__item food-grid__item--red" role="img" aria-label="Foto de canapés"></div>
      <div class="food-grid__item" role="img" aria-label="Foto de salgados dourados"></div>
      <div class="food-grid__item" role="img" aria-label="Foto de salgados assados"></div>
      <div class="food-grid__item food-grid__item--red" role="img" aria-label="Foto de canapés"></div>
      <div class="food-grid__item" role="img" aria-label="Foto de tortinhas"></div>
      <div class="food-grid__item food-grid__item--brown" role="img" aria-label="Foto de doces de chocolate"></div>
      <div class="food-grid__item food-grid__item--brown" role="img" aria-label="Foto de doces de chocolate"></div>
      <div class="food-grid__item food-grid__item--red" role="img" aria-label="Foto de canapés"></div>
      <div class="food-grid__item" role="img" aria-label="Foto de salgados fritos"></div>
      <div class="food-grid__item" role="img" aria-label="Foto de salgados dourados"></div>
    </div>

    <section class="contact">
      <h2 class="contact__title">Contato</h2>
      <div class="contact__row">
        <svg class="contact__icon" viewBox="0 0 12 12"><path d="M2 1l2 0 1 3-1.5 1a6 6 0 0 0 3.5 3.5L8 7l3 1v2c0 .6-.4 1-1 1A9 9 0 0 1 1 2c0-.6.4-1 1-1z" fill="var(--red)"/></svg>
        <span class="contact__phone">00 0 9999-9999</span>
      </div>
      <div class="contact__row">
        <svg class="contact__icon" viewBox="0 0 12 12"><path d="M2 1l2 0 1 3-1.5 1a6 6 0 0 0 3.5 3.5L8 7l3 1v2c0 .6-.4 1-1 1A9 9 0 0 1 1 2c0-.6.4-1 1-1z" fill="var(--red)"/></svg>
        <span class="contact__phone">00 0000-0000</span>
      </div>
      <div class="contact__row">
        <svg class="contact__icon" viewBox="0 0 12 12"><rect x="1" y="3" width="10" height="7" fill="none" stroke="var(--red)" stroke-width="1.2"/><path d="M1 3l5 4 5-4" fill="none" stroke="var(--red)" stroke-width="1.2"/></svg>
        <span class="contact__line">contato@espacoaurora.com.br</span>
      </div>
      <p class="contact__address">Rua das Acácias, 120 · Centro<br>Cidade Nova · SP</p>
    </section>

    <p class="cover-tagline">Qualidade, requinte, segurança e bom atendimento para seu evento</p>
    <span class="brand-name brand-name--cover">Espaço Aurora</span>
  </main>
</body>
</html>
```